full stationary design for a modern sleek design company

we are a design company that does modern minimalistic interior design works as well as other design services for high end clients.
we need a full stationary design including and not limited to (double sided business card, letter head, envelopes, documents folder...etc) that reflects the modern style design we do.
sleek modern and minimalistic is the requirements.
Updates

please use the latest attached files as there was a slight modification on the logo Added Wednesday, March 1, 2017

minor update on the logo files in JPG and PSD has been updated kindly follow the new attachments. Added Thursday, March 2, 2017

Target Market(s)

modern minimalist clients

Industry/Entity Type

Design Agency

Requirements
Must have
• the logo
Nice to have
• i like the colors in the colored 3D logo attached
Should not have
• too many colors

```html
<!DOCTYPE html>
<html lang="en">
<head>
<meta charset="utf-8">
<title>Halvard Studio – Business Card</title>
<link rel="stylesheet" href="https://fonts.googleapis.com/css2?family=Open+Sans:wght@400;600&display=swap">
<style>
  :root {
    --orange: #f7941d;
    --ink: #3a3a3a;
    --text: #444444;
    --card-white: #ffffff;
    --edge-dark: #3d4347;
    --backdrop: #e9e7e4;
  }
  * { margin: 0; padding: 0; box-sizing: border-box; }
  html, body { width: 1200px; height: 987px; overflow: hidden; }
  body {
    position: relative;
    background: var(--backdrop);
    font-family: "Open Sans", Arial, sans-serif;
    color: var(--text);
  }
  .card {
    position: absolute;
    width: 615px;
    height: 351px;
    box-shadow: 0 4px 10px rgba(0,0,0,0.18);
  }
  .card-front { left: 293px; top: 130px; background: var(--card-white); }
  .card-back { left: 292px; top: 505px; background: var(--orange); }

  .brand {
    position: absolute;
    display: flex;
    align-items: center;
    gap: 10px;
    font-weight: 600;
    letter-spacing: 2px;
    text-transform: uppercase;
    white-space: nowrap;
  }
  .brand-mark { display: block; }
  .card-front .brand {
    right: 38px; top: 58px;
    font-size: 30px; color: var(--ink);
  }
  .card-front .brand-mark { width: 26px; height: 26px; background: var(--orange); }
  .card-back .brand {
    left: 50%; top: 50%;
    transform: translate(-50%, -50%);
    font-size: 38px; color: var(--card-white);
  }
  .card-back .brand-mark { width: 32px; height: 32px; background: var(--card-white); }

  .holder-name {
    position: absolute; left: 29px; top: 192px;
    font-size: 21px; font-weight: 600; color: var(--orange);
    letter-spacing: 0.3px;
  }
  .holder-role {
    position: absolute; left: 29px; top: 219px; right: 38px;
    display: flex; align-items: center; gap: 2px;
    font-size: 16px; color: var(--ink);
  }
  .holder-role::after {
    content: ""; flex: 1; height: 1px; background: var(--ink); margin-top: 2px;
  }

  .contact-list {
    position: absolute; left: 29px; top: 250px;
    list-style: none; font-size: 16px; line-height: 24px;
  }
  .contact-list li { display: flex; align-items: center; gap: 8px; }
  .contact-icon { width: 14px; height: 14px; fill: var(--orange); flex: none; }

  .studio-address {
    position: absolute; right: 38px; top: 250px;
    text-align: right; font-style: normal; font-size: 16px; line-height: 23px;
  }

  .edge-accent {
    position: absolute; left: 0; right: 0; bottom: 8px;
    height: 3px; background: var(--orange);
  }
  .edge-base {
    position: absolute; left: 0; right: 0; bottom: 0;
    height: 8px; background: var(--edge-dark);
  }
</style>
</head>
<body>

<section class="card card-front" aria-label="Business card front">
  <div class="brand"><span class="brand-mark"></span>Halvard Studio</div>

  <h1 class="holder-name">ELIAS BRANDT</h1>
  <p class="holder-role">CEO&amp;Founder</p>

  <ul class="contact-list">
    <li>
      <svg class="contact-icon" viewBox="0 0 24 24" aria-hidden="true"><path d="M6.6 10.8a15.1 15.1 0 0 0 6.6 6.6l2.2-2.2c.3-.3.7-.4 1-.2 1.1.4 2.3.6 3.6.6.6 0 1 .4 1 1V20c0 .6-.4 1-1 1C10.6 21 3 13.4 3 4c0-.6.4-1 1-1h3.5c.6 0 1 .4 1 1 0 1.3.2 2.5.6 3.6.1.3 0 .7-.2 1z"/></svg>
      (555) 214 0386
    </li>
    <li>
      <svg class="contact-icon" viewBox="0 0 24 24" aria-hidden="true"><path d="M8 1h8a2 2 0 0 1 2 2v18a2 2 0 0 1-2 2H8a2 2 0 0 1-2-2V3a2 2 0 0 1 2-2zm0 3v14h8V4zm4 15.5a1 1 0 1 0 0 2 1 1 0 0 0 0-2z"/></svg>
      (555) 730 1192
    </li>
    <li>
      <svg class="contact-icon" viewBox="0 0 24 24" aria-hidden="true"><path d="M2 5h20v14H2zm2 2v.5l8 5 8-5V7zm0 2.8V17h16V9.8l-8 5z"/></svg>
      elias@halvardstudio.com
    </li>
  </ul>

  <address class="studio-address">
    1420 Alder Court<br>
    Juneau, Alaska 99801<br>
    www.halvardstudio.com
  </address>

  <div class="edge-accent"></div>
  <div class="edge-base"></div>
</section>

<section class="card card-back" aria-label="Business card back">
  <div class="brand"><span class="brand-mark"></span>Halvard Studio</div>
</section>

</body>
</html>
```